Young judge needs a website to publish and to connect

I would like to have a website where I can publish my articles in public law. I am judge at the Alpine Civic Review Tribunal. Therefore, the website must have a calm, friendly and fairly neutral design. Also, it should be mobile friendly and easy to use.

On my website, I want to

- publish articles such as https://www.brindlepost.example/pulse/how-win-court-tobias-wenger/ and get feedbacks from my colleagues
- generate interest for my project on 'Statutes and Society - Notes from the Chamber', a book that I would like to publish in 2020 and which brings together my publications on public law (http://www.civicnorm.example/content/english/profil/publikationen.html ).
- provide updates for my university courses on constitutional, administrative and international law.

For that purpose, I would kindly ask you to suggest a website that communicates a fresh approach to the work of a young judge in constitutional and administrative law. Please have in mind that I do not only sit on the bench, but that I also work in academia. Therefore, it should be suitable for an audience from both university and law practice. The website should replace the existing website on www.civicnorm.example that I designed when still working as a lawyer. Thank you.

Target Market(s)

Academica, law firms, courts

Industry/Entity Type

University

Contact Information for Business Card

Tobias Wenger
Judge
Alpine Civic Review Tribunal
M +41 79 5XX 8X 2X

Logo Text

Notes from the Chamber

Number of Pages Required

5+ page

Font styles to use
Sans Serif

Colors
0455a3

Requirements
Must have
• - a page where I can publish and get feedbacks
• - a page about my project on law and politics
• - a page where I can provide updates for my university courses on constitutional, administrative and international law
• - page where I can list current and planned projects
• - a collaborative, young and fresh approach
Nice to have
• - a page reserved for my colleagues at the Alpine Civic Review Tribunal where I can alert them about to possibility to collaborate (if possibly password protected) and where they may suggest what to contribute to a specific project
Should not have
• anything which might to suggest that I want to make money with it, bragging or pretentious. Do not forget: I am judge, not a barrister.

```html
<!DOCTYPE html>
<html lang="en">
<head>
<meta charset="utf-8">
<title>Tobias Wenger – Expert in Public Law</title>
<link rel="stylesheet" href="https://fonts.googleapis.com/css2?family=Lato:wght@400&display=swap">
<style>
  :root {
    --nav-bg: #131313;
    --text-light: #ffffff;
    --accent: #0455a3;
    --accent-soft: #1a8fd0;
    --hero-dark: #1c1d1f;
    --hero-mid: #3a3b3d;
    --hero-light: #5c5d60;
  }
  * { margin: 0; padding: 0; box-sizing: border-box; }
  html, body {
    width: 1200px;
    height: 825px;
    overflow: hidden;
    background: var(--nav-bg);
    font-family: "Lato", sans-serif;
    color: var(--text-light);
  }
  .page { position: relative; width: 1200px; height: 825px; }

  .site-header {
    position: absolute; top: 0; left: 0;
    width: 1200px; height: 118px;
    background: var(--nav-bg);
    z-index: 2;
  }
  .nav-link {
    position: absolute;
    top: 53px;
    font-size: 19px;
    letter-spacing: 0.2px;
    color: var(--text-light);
    text-decoration: none;
    white-space: nowrap;
  }
  .nav-profile      { left: 36px; top: 55px; }
  .nav-projects     { left: 156px; top: 55px; }
  .nav-publications { left: 301px; }
  .nav-courses      { left: 751px; }
  .nav-collaborate  { left: 889px; }
  .nav-contact      { left: 1072px; }

  .brand {
    position: absolute;
    left: 600px; top: 22px;
    transform: translateX(-50%);
    display: flex; flex-direction: column; align-items: center;
    text-decoration: none;
  }
  .brand-mark {
    width: 26px; height: 26px;
    background: var(--accent-soft);
    margin-bottom: 10px;
  }
  .brand-name {
    font-size: 27px;
    color: var(--text-light);
    white-space: nowrap;
    line-height: 1;
  }

  .hero {
    position: absolute; top: 118px; left: 0;
    width: 1200px; height: 707px;
  }
  .hero-photo {
    position: absolute; inset: 0;
    background:
      radial-gradient(ellipse at 50% 15%, var(--hero-light) 0%, transparent 55%),
      linear-gradient(180deg, var(--hero-mid) 0%, var(--hero-dark) 75%);
  }
  .hero-title {
    position: absolute;
    left: 127px; top: 272px;
    font-size: 93px;
    font-weight: 400;
    line-height: 1;
    letter-spacing: 0.5px;
    white-space: nowrap;
  }
  .hero-rule {
    position: absolute;
    left: 129px; top: 366px;
    width: 921px; height: 2px;
    background: var(--accent-soft);
  }

  .social {
    position: absolute;
    left: 600px; top: 626px;
    transform: translateX(-50%);
    display: flex; gap: 22px;
  }
  .social-link {
    display: flex; align-items: center; gap: 8px;
    color: var(--text-light);
    text-decoration: none;
    font-size: 16px;
  }
  .social-dot {
    width: 50px; height: 50px;
    border-radius: 50%;
    background: var(--accent);
  }
  .social-dot.is-light { background: var(--accent-soft); }
</style>
</head>
<body>
<div class="page">
  <header class="site-header">
    <nav>
      <a class="nav-link nav-profile" href="#profile">PROFILE</a>
      <a class="nav-link nav-projects" href="#projects">PROJECTS</a>
      <a class="nav-link nav-publications" href="#publications">PUBLICATIONS</a>
      <a class="brand" href="#home">
        <span class="brand-mark"></span>
        <span class="brand-name">Tobias Wenger</span>
      </a>
      <a class="nav-link nav-courses" href="#courses">COURSES</a>
      <a class="nav-link nav-collaborate" href="#collaborate">COLLABORATE</a>
      <a class="nav-link nav-contact" href="#contact">CONTACT</a>
    </nav>
  </header>

  <section class="hero">
    <div class="hero-photo" role="img" aria-label="Photograph of four young men in dark pinstripe suits walking together, darkened as a background"></div>
    <h1 class="hero-title">EXPERT IN PUBLIC LAW</h1>
    <div class="hero-rule"></div>
    <div class="social">
      <a class="social-link" href="https://www.brindlepost.example/in/tobias-wenger/">
        <span class="social-dot"></span>Brindlepost
      </a>
      <a class="social-link" href="#chirrup">
        <span class="social-dot is-light"></span>Chirrup
      </a>
    </div>
  </section>
</div>
</body>
</html>
```